Ready to be wowed! Snazzy, sassy, classy Realtor seeking Web banner for unique innovative Realtor!

Placer County Realtor need web banner re-design. Looking for classy, classic, clean design appealing to elite prospects. Previous focus was short sales now looking to gear towards listing and selling homes, remove short sale focus. Must include, license # 04729318, HR logo, phone, email, etc. check out LiaPorter.com for reference info. I am open to suggestions for other needed content for THE BEST WEB BANNER ON EARTH! LOL. I really want to appeal to the upscale clients, also will be getting away from orange colors going more to a green. Please contact me at LiaPorterSells@mailvista.com for more info
measurements of banner; Images of exactly 960 × 120 pixels will be used as-is. It's Wordpress Genesis.
Updates

I'm really looking for something clean that looks upscale and luxury, classy. 

Please update email address to lia@liaporter.com

Reason: I still haven't gotten what I want. I noticed some really good designs closer to the end here, I'm hoping to allow those folks and maybe a few new ones the opportunity to give me exactly what I want! Thanks!

Reason: I still don't have what I want. I want a simple design that shows that I am a Realtor, maybe a picture of a house???? or something related to real estate. Less emphasis on the Halverson Realty logo. Classy and upscale. Fonts should be easy to read but not so simply boring. Please, please, please read the brief!! I REALLY want a good banner!!

Please take a look at the site color adjustment. That's what color it will stay. www.LiaPorter.com

Reason: I'm ready to move this to the end now. I need a design. I'm extending hopefully only this last time to take a vote on them. I will be reaching out to a few select designers to make a few modifications. I appreciate everyone's time on this as you know this is a very tough and important decision to make.

Reason: Need more input

Reason: still trying to decide

Target Market(s)

upscale home sellers

Industry/Entity Type

Realtor

Requirements
Must have
• License # 04729318
Phone (555)304-2871
HR LOGO (attached)
areas of service- Roseville, Rocklin, Granite Bay
LiaPorterSells@mailvista.com

```html
<!DOCTYPE html>
<html lang="en">
<head>
<meta charset="utf-8">
<title>Lia Porter – Realtor</title>
<link rel="stylesheet" href="https://fonts.googleapis.com/css2?family=Kaushan+Script&family=Advent+Pro:wght@300;400&family=Arimo&display=swap">
<style>
  :root {
    --bg-center: #4b4b4b;
    --bg-edge: #161616;
    --name-green: #8fd63c;
    --name-outline: #1c2a10;
    --accent-green: #2fd62f;
    --text-green: #7ed63a;
    --contact-white: #f2f2f2;
    --brand-blue: #1d4f9c;
    --photo-warm: #c9a57a;
    --photo-leaf: #6f8a4a;
  }
  html, body {
    margin: 0;
    padding: 0;
    overflow: hidden;
    background: #111;
  }
  .banner {
    position: relative;
    width: 1200px;
    height: 150px;
    overflow: hidden;
    background: radial-gradient(ellipse 70% 120% at 35% 40%, var(--bg-center), var(--bg-edge));
    font-family: "Advent Pro", sans-serif;
  }
  .agent-name {
    position: absolute;
    left: 14px;
    top: 4px;
    margin: 0;
    font-family: "Kaushan Script", cursive;
    font-weight: 400;
    font-size: 78px;
    line-height: 1.1;
    color: var(--name-green);
    -webkit-text-stroke: 2px var(--name-outline);
    text-shadow: 3px 3px 4px rgba(0,0,0,.6);
    white-space: nowrap;
  }
  .license {
    position: absolute;
    left: 138px;
    top: 108px;
    font-size: 27px;
    font-weight: 400;
    color: var(--text-green);
    letter-spacing: .5px;
  }
  .brokerage {
    position: absolute;
    left: 328px;
    top: 90px;
    display: flex;
    align-items: center;
    gap: 6px;
  }
  .brokerage-mark {
    width: 14px;
    height: 14px;
    background: var(--brand-blue);
  }
  .brokerage-name {
    font-family: "Advent Pro", sans-serif;
    font-weight: 400;
    font-size: 17px;
    line-height: 1.05;
    color: var(--contact-white);
    width: 70px;
  }
  .service-area {
    position: absolute;
    font-family: "Arimo", sans-serif;
    font-size: 22px;
    color: var(--accent-green);
    text-shadow: 0 0 1px #000;
    margin: 0;
    white-space: nowrap;
  }
  .service-area.line-1 { left: 410px; top: 12px; }
  .service-area.line-2 { left: 487px; top: 46px; }
  .service-area.line-3 { left: 646px; top: 80px; }
  .agent-photo {
    position: absolute;
    left: 821px;
    top: 12px;
    width: 79px;
    height: 126px;
    background: linear-gradient(160deg, var(--photo-leaf), var(--photo-warm) 55%, #e8d3b3);
  }
  .contact {
    position: absolute;
    left: 910px;
    width: 285px;
    text-align: center;
    color: var(--contact-white);
    font-weight: 300;
    white-space: nowrap;
  }
  .contact.phone { top: 24px; font-size: 25px; }
  .contact.email { top: 76px; font-size: 21px; }
</style>
</head>
<body>
  <div class="banner">
    <h1 class="agent-name">Lia Porter</h1>
    <div class="license">LICENSE#04729318</div>
    <div class="brokerage">
      <span class="brokerage-mark"></span>
      <span class="brokerage-name">Halverson Realty</span>
    </div>
    <p class="service-area line-1">Serving Roseville,</p>
    <p class="service-area line-2">Rocklin,</p>
    <p class="service-area line-3">Granite Bay</p>
    <div class="agent-photo" role="img" aria-label="Portrait photo of the agent"></div>
    <div class="contact phone">555.304.2871</div>
    <div class="contact email">LIAPORTERSELLS@MAILVISTA.COM</div>
  </div>
</body>
</html>
```